Business card design needed

Hello, I Need a business card for a company that specialises in providing contract management services for civil construction projects - roads, bridges etc.
I do have a logo that i produced for PLOVER Civilworks however it probably needs a little work, the circles dont have defined edges, i was thinking the colours should reflect the dry interior of Australia progressing out to the colours of the ocean as you move towards the East.... that was my thinking anyway!
Target Market(s)
Professional people generally 30+ yrs old who need professional services to deliver contracts in a high risk environment
Industry/Entity Type
Construction
Contact Information for Business Card
PLOVER Civilworks
Darren Pollock - Director and Principal Engineer
Registered Professional Engineer of Queensland
Phone 0491 265 807
Email darren@plovercivilworks.com.au
ABN 48 213 670 194
Logo Text
PLOVER Civilworks
Logo styles of interest
Pictorial/Combination Logo
Wordmark Logo
Lettermark Logo
Look and feel

```html
<!DOCTYPE html>
<html lang="en">
<head>
<meta charset="utf-8">
<title>PLOVER Civilworks – Business Card</title>
<link rel="stylesheet" href="https://fonts.googleapis.com/css2?family=Roboto+Condensed:wght@400;700&display=swap">
<style>
  :root {
    --page-bg: #ecebe6;
    --card-cream: #f7f1c8;
    --card-light: #fffbe6;
    --corner-grey: #c9c9c9;
    --corner-edge: #e6e4da;
    --ink: #1c1c1c;
    --ink-soft: #3a3a3a;
    --brand-ink: #3f3f3f;
  }
  * { margin: 0; padding: 0; box-sizing: border-box; }
  html, body {
    width: 1200px;
    height: 871px;
    overflow: hidden;
    background: var(--page-bg);
    font-family: "Roboto Condensed", "Arial Narrow", sans-serif;
  }
  .canvas {
    position: relative;
    width: 1200px;
    height: 871px;
  }
  .business-card {
    position: absolute;
    left: 150px;
    top: 185px;
    width: 900px;
    height: 500px;
    overflow: hidden;
    background: radial-gradient(ellipse at 62% 30%, var(--card-light) 0%, var(--card-cream) 70%);
    box-shadow: 0 10px 30px rgba(0, 0, 0, 0.18);
  }
  .corner-swoosh {
    position: absolute;
    inset: 0;
    width: 100%;
    height: 100%;
  }
  .brand {
    position: absolute;
    left: 60px;
    top: 68px;
  }
  .brand-name {
    font-size: 44px;
    font-weight: 400;
    color: var(--brand-ink);
    letter-spacing: 0.3px;
    line-height: 1;
  }
  .person {
    position: absolute;
    left: 60px;
    top: 170px;
    color: var(--ink);
  }
  .person-name {
    font-size: 38px;
    font-weight: 700;
    line-height: 1.05;
  }
  .person-title {
    font-size: 15px;
    font-weight: 400;
    color: var(--ink-soft);
    margin-top: 2px;
  }
  .contact {
    position: absolute;
    left: 60px;
    top: 275px;
    color: var(--ink);
    font-size: 30px;
    line-height: 46px;
  }
  .contact-label { font-weight: 700; margin-right: 6px; }
  .contact-value { font-weight: 400; }
  .contact-abn { font-weight: 700; }
</style>
</head>
<body>
  <main class="canvas">
    <section class="business-card" aria-label="PLOVER Civilworks business card">
      <svg class="corner-swoosh" viewBox="0 0 900 500" preserveAspectRatio="none" aria-hidden="true">
        <path d="M900 80 C 880 260, 820 400, 690 500 L 900 500 Z" fill="var(--corner-grey)"/>
        <path d="M900 80 C 880 260, 820 400, 690 500" fill="none" stroke="var(--corner-edge)" stroke-width="6"/>
      </svg>

      <div class="brand">
        <p class="brand-name">PLOVER Civilworks</p>
      </div>

      <div class="person">
        <p class="person-name">Darren Pollock</p>
        <p class="person-title">Director and Principal Engineer Registered Professional Engineer of Queensland</p>
      </div>

      <div class="contact">
        <p><span class="contact-label">Phone</span><span class="contact-value">0491 265 807</span></p>
        <p><span class="contact-label">Email</span><span class="contact-value">darren@plovercivilworks.com.au</span></p>
        <p class="contact-abn">ABN 48 213 670 194</p>
      </div>
    </section>
  </main>
</body>
</html>
```